Web Site Design For Real Estate Sales Project

The idea behind this project is pretty simple. I am putting my penthouse apartment up for sale and am trying to be creative in selling it.
Technically this will be pretty simple, it will be 3 pages but graphically this has to be as impressive as possible which is why I am trying Pixel Harbor.
The apartment is located in Barra Da Tijuca, Rio De Janeiro, Brazil. (This is where the 2016 Meridian Regatta will be held)
I am looking for an index page and 2 sub-pages. I am open to all kinds of designs and navigation's but it has to make an impression quickly with a professional and enticing design. The index page should make it obvious that there is a penthouse apartment for sale in Barra Da Tijuca ( suburb of Rio De Janeiro). The first sub page is about the Condominium where the apartment is located, the second sub page is about the apartment itself.
Here is a more detailed description of what the 3 pages should be about.
Index Page
This is the landing page and should make it obvious that there is an apartment for sale in Barra Da Tijuca, Rio De Janeiro with the following attributes
251 SQ M
Duplex Penthouse
4 suites
Price R$ 2.200.000
Price per SQ M: R$ 8.764
First Sub-Page
This is about the Condominium which is called "Gentle Palm Residences" with the following bullets
*Family friendly and safe
*Direct access to the beach
*Many amenities like pool, football court, gym, sauna
There should be some photos of the condominium and a link to the site of the condominium ( www.gprvx.com )
Second Sub-page
This is about the apartment. It should list in bullets the features of the apartment and then have a photo gallery of the view and various rooms. I have attached sample photos but will eventually have to use more photos.
Apartment Features
Price: R$ 2.220.000
251 m2 Duplex Penthouse
4 suites
maids room with bath
guest bathroom
living room
dinning room
Terrace with heated pool for year round use
Veranda
As mentioned above I am open to all designs and navigation so feel free to be creative. The important thing is catch peoples attention and get the message across in a few seconds, which is that there is an apartment for sale at this price with these features in this location. I will then use brightlist promoter and SEO to get people to the site.
Thanks
Target Market(s)
Men and Women from 30-60 years of age.
Industry/Entity Type
Apartment

```html
<!DOCTYPE html>
<html lang="en">
<head>
<meta charset="utf-8">
<title>Coastline Penthouse – About the Apartment</title>
<link rel="stylesheet" href="https://fonts.googleapis.com/css2?family=Marcellus&family=Arimo:wght@400;700&display=swap">
<style>
:root{
  --deep:#0b1f17;
  --lime:#9ccd2c;
  --gold:#f5b70f;
  --gold-dark:#e0a000;
  --white:#ffffff;
  --line:rgba(160,200,90,.35);
  --social:#1f5db5;
}
*{margin:0;padding:0;box-sizing:border-box}
html,body{width:1200px;height:675px;overflow:hidden;background:var(--deep)}
body{font-family:"Arimo",Arial,sans-serif;color:var(--white);position:relative}

.site-header{
  position:absolute;left:0;top:0;width:1200px;height:128px;
  background:
    radial-gradient(ellipse 420px 160px at 640px 20px,rgba(190,230,110,.45),transparent 70%),
    repeating-linear-gradient(90deg,rgba(255,255,255,.05) 0 22px,rgba(0,0,0,.06) 22px 44px,rgba(255,255,255,.03) 44px 58px),
    linear-gradient(90deg,#123a37 0%,#2f6a33 30%,#5f9a35 52%,#3d7430 72%,#163c38 100%);
  border-bottom:1px solid var(--line);
}
.brand{
  position:absolute;left:160px;top:39px;width:380px;
  font-family:"Marcellus",serif;font-size:34px;line-height:40px;color:var(--lime);
  white-space:nowrap;
}
.home-icon{position:absolute;left:558px;top:38px;width:48px;height:42px}
.main-nav a{
  position:absolute;top:45px;height:35px;line-height:35px;
  border-radius:8px;font-size:13px;text-align:center;text-decoration:none;white-space:nowrap;
  color:var(--white);background:linear-gradient(#5c5c5c,#3a3a3a);
  border:1px solid #2a2a2a;box-shadow:inset 0 1px 0 rgba(255,255,255,.25);
}
.main-nav a.active{background:linear-gradient(#ffd23a,var(--gold-dark));color:#1b1b1b;border-color:#b98400}

.content{
  position:absolute;left:0;top:129px;width:1200px;height:464px;
  background:
    radial-gradient(ellipse 500px 300px at 700px 520px,rgba(120,170,50,.55),transparent 70%),
    repeating-linear-gradient(90deg,rgba(255,255,255,.025) 0 30px,transparent 30px 60px),
    linear-gradient(180deg,#0d2a22 0%,#163524 45%,#2f5320 100%);
}
.features-title{
  position:absolute;left:163px;top:78px;
  font-family:"Marcellus",serif;font-size:28px;font-weight:400;color:var(--gold);
}
.price{position:absolute;left:163px;top:116px;font-size:22px;font-weight:700;letter-spacing:.5px}
.feature-list{position:absolute;left:163px;top:179px;list-style:none;font-size:13px}
.feature-list li{position:relative;padding-left:24px;height:26px;line-height:15px}
.feature-list li svg{position:absolute;left:0;top:2px}
.divider{position:absolute;left:455px;top:12px;width:1px;height:424px;background:var(--line)}

.photo{
  position:absolute;width:254px;height:150px;border:5px solid var(--white);
  box-shadow:0 14px 12px -6px rgba(0,0,0,.6);
}
.photo-beach{left:492px;top:56px;background:linear-gradient(180deg,#9fb8c8 0%,#8a9a8a 35%,#d8d2c0 65%,#3f8a9a 100%)}
.photo-entrance{left:786px;top:56px;background:linear-gradient(160deg,#b9c4d2 0%,#8a6a52 40%,#a9a9a9 75%,#cfcfcf 100%)}
.photo-terrace{left:492px;top:246px;background:linear-gradient(180deg,#dfe6ea 0%,#a9b2b6 45%,#d2d2cc 100%)}
.photo-coast{left:786px;top:246px;background:linear-gradient(180deg,#8fb4da 0%,#2f6f9f 40%,#6f8a6a 70%,#4d6a3a 100%)}

.site-footer{
  position:absolute;left:0;top:593px;width:1200px;height:82px;
  background:linear-gradient(90deg,#0e2a24,#1b3b26 50%,#0e2a24);
  border-top:1px solid var(--line);
}
.copyright{position:absolute;left:160px;top:16px;font-size:11px;color:#e8e8e8;white-space:nowrap}
.copyright strong{font-size:15px;font-weight:700;color:var(--white);margin-right:3px}
.footer-divider{position:absolute;top:8px;width:1px;height:68px;background:var(--line)}
.contact-row{position:absolute;left:515px;display:flex;align-items:center;white-space:nowrap}
.contact-row .label{font-family:"Marcellus",serif;font-size:18px;width:80px;margin-left:11px}
.label em,.follow em{font-style:normal;color:var(--lime)}
.phone-number{font-size:25px;font-weight:700}
.email{font-size:13px;font-weight:700}
.follow{position:absolute;left:845px;top:22px;font-family:"Marcellus",serif;font-size:27px}
.social{position:absolute;left:975px;top:25px;display:flex;align-items:center;gap:8px;font-size:13px}
.social .dot{width:36px;height:36px;border-radius:50%;background:var(--social)}
</style>
</head>
<body>
<header class="site-header">
  <div class="brand">Coastline Penthouse</div>
  <svg class="home-icon" viewBox="0 0 48 42" aria-label="Home">
    <path d="M24 3 L45 21 L40 21 L40 40 L29 40 L29 28 L19 28 L19 40 L8 40 L8 21 L3 21 Z" fill="#e9e9e9" stroke="#6f6f6f" stroke-width="2" stroke-linejoin="round"/>
  </svg>
  <nav class="main-nav">
    <a href="#" style="left:622px;width:168px">Gentle Palm Residences</a>
    <a href="#" class="active" style="left:806px;width:138px">About the Apartment</a>
    <a href="#" style="left:959px;width:81px">Contact Us</a>
  </nav>
</header>

<main class="content">
  <h1 class="features-title">Apartment Features</h1>
  <p class="price">R$ 2.200.000</p>
  <ul class="feature-list">
    <li><svg width="15" height="11" viewBox="0 0 15 11"><path d="M0 3.5h8V0l7 5.5-7 5.5V7.5H0z" fill="#9ccd2c"/></svg>251 m2 Duplex Penthouse</li>
    <li><svg width="15" height="11" viewBox="0 0 15 11"><path d="M0 3.5h8V0l7 5.5-7 5.5V7.5H0z" fill="#9ccd2c"/></svg>4 suites</li>
    <li><svg width="15" height="11" viewBox="0 0 15 11"><path d="M0 3.5h8V0l7 5.5-7 5.5V7.5H0z" fill="#9ccd2c"/></svg>Maids room with bath</li>
    <li><svg width="15" height="11" viewBox="0 0 15 11"><path d="M0 3.5h8V0l7 5.5-7 5.5V7.5H0z" fill="#9ccd2c"/></svg>Guest bathroom</li>
    <li><svg width="15" height="11" viewBox="0 0 15 11"><path d="M0 3.5h8V0l7 5.5-7 5.5V7.5H0z" fill="#9ccd2c"/></svg>Living room</li>
    <li><svg width="15" height="11" viewBox="0 0 15 11"><path d="M0 3.5h8V0l7 5.5-7 5.5V7.5H0z" fill="#9ccd2c"/></svg>Dinning room</li>
    <li><svg width="15" height="11" viewBox="0 0 15 11"><path d="M0 3.5h8V0l7 5.5-7 5.5V7.5H0z" fill="#9ccd2c"/></svg>Terrace with heated pool for year round use<br>Veranda</li>
  </ul>
  <div class="divider"></div>

  <div class="photo photo-beach" role="img" aria-label="Aerial view of the beachfront towers and ocean waves"></div>
  <div class="photo photo-entrance" role="img" aria-label="Condominium entrance gate with driveway"></div>
  <div class="photo photo-terrace" role="img" aria-label="Rooftop terrace with parasols, tables and chairs"></div>
  <div class="photo photo-coast" role="img" aria-label="Panoramic view of the coastline and lagoon from the hills"></div>
</main>

<footer class="site-footer">
  <p class="copyright"><strong>Coastline Penthouse</strong>© 2013. All Right Reserved.</p>
  <div class="footer-divider" style="left:483px"></div>
  <div class="contact-row" style="top:11px">
    <svg width="24" height="22" viewBox="0 0 24 22"><path d="M2 7c0-3 4-5 10-5s10 2 10 5v2h-5V7H7v2H2z M6 10h12l3 10H3z" fill="#9ccd2c"/><circle cx="12" cy="15" r="3" fill="#1b3b26"/></svg>
    <span class="label">Call <em>us :</em></span>
    <span class="phone-number">812 306 497</span>
  </div>
  <div class="contact-row" style="top:48px">
    <svg width="24" height="18" viewBox="0 0 24 18"><rect x="1" y="1" width="22" height="16" rx="1" fill="#f5b70f"/><path d="M1 1l11 9 11-9" fill="none" stroke="#b98400" stroke-width="1.5"/></svg>
    <span class="label">Mail <em>us :</em></span>
    <span class="email">info@coastline-home.net</span>
  </div>
  <div class="footer-divider" style="left:820px"></div>
  <div class="follow">Follow <em>us</em></div>
  <div class="social"><span>Friendloop</span><span class="dot"></span></div>
</footer>
</body>
</html>
```